TK VESSA
transformative skincare
plant-based | clean | anti-aging
The line is for both men and women
-luxurious feeling, plant-based, all natural skincare line
This is a continuation from previous project but maybe with sans serif or serif font instead of cursive for the TK part of Vessa. (Please see logo designs from 2 years ago)
- I think TK Vessa should be smaller in size than the names of the product so people can more easily read what it says since there are a lot of products in a set.
Also, the day products will have very light cream almost white colored labels with dark green and gold fonts/accents and the night products will have dark green almost black labels with light cream and gold colored font I think.

The products are for both men and women so I don't want the labels looking too feminine? Maybe more simple or a faint leaf design in background.

-about 24 different labels for skincare jars and bottles:
Glycolic Cleanser 4oz and 8oz
Cleansing Oil 4oz and 8oz
Vitamin C Day Serum 1oz and 2oz
Stem Cell C Day Serum 1oz and 2oz
Stem Cell Day Cream 2oz and 4oz
Retinol Night Serum - Lavender 1oz and 2oz
Retinol Night Serum - Neroli 1oz and 2oz
Coconut Charcoal Scrub 2oz and 4oz
Enzyme Night Cream 2oz and 4oz
Eye Renewal Night Serum .5oz
Vitamin C Day Eye Cream .5oz
Honey Lip Balm .5oz
Enzyme Body Lotion - Vanilla Almond 8oz
Enzyme Body Lotion - Mango Lime 8oz
Enzyme Body Lotion - Lavender 8oz

Target Market(s)

ages 40-50 with some 20's and 30's sprinkled in

Industry/Entity Type

Beauty and Skincare

Font styles to use
Serif
Sans Serif
Other font styles liked:
• If you have a more unique but clean or slick font or combo of fonts in mind, please be creative!

Colors
00AB8E
00BBA5
67D7C9
C6EFE9
E9F9F6
FFF300
FFF600
FEFA6F
FFFEC7
FFFEE8

Requirements
Must have
• TK Vessa should be smaller in size than the names of the product so people can more easily read what it says since there are a lot of products in a set. day products will be light colored labels with dark green and gold fonts/accents and the night products will be on dark green labels with light cream and gold colored font
Nice to have
• Attached are original files of a logo previously designed a couple years ago but not sure I want the script TK anymore? Some sort of leaf design to go with previously made logo but want to see TK in serif or sans serif instead of script. Also attached are simple labels on the products currently and how they look as they're being sold to private clients. Wanting to put them out online for the public this year so need high end, luxurious look and feel but not generic. Thank you!
Should not have
• too busy of a design

```html
<!DOCTYPE html>
<html lang="en">
<head>
<meta charset="utf-8">
<title>TK Vessa — Label Set</title>
<link rel="stylesheet" href="https://fonts.googleapis.com/css2?family=Cinzel:wght@400;700&family=Montserrat:wght@500&display=swap">
<style>
  :root {
    --page: #dcdcdc;
    --cream: #f8f5f0;
    --forest: #1b3529;
    --sage: #5b6f61;
    --gold: #b68a55;
    --gold-light: #d4a873;
    --gold-deep: #98693a;
    --leaf-day: rgba(190, 190, 180, 0.45);
    --leaf-night: rgba(90, 110, 70, 0.35);
  }
  * { margin: 0; padding: 0; box-sizing: border-box; }
  html, body { width: 940px; height: 1200px; overflow: hidden; background: var(--page); }
  .label-set { position: relative; width: 940px; height: 1200px; }

  .label {
    position: absolute;
    overflow: hidden;
    font-size: var(--fs);
    text-align: center;
    box-shadow: 0 2px 8px rgba(0, 0, 0, 0.12);
  }
  .label--day { background: var(--cream); }
  .label--night { background: var(--forest); }

  .label__leaf {
    position: absolute;
    left: 22%; top: -4%;
    width: 70%; height: 110%;
    border-radius: 50% 50% 45% 55%;
    transform: rotate(28deg);
  }
  .label--day .label__leaf { background: radial-gradient(ellipse at center, var(--leaf-day), transparent 70%); }
  .label--night .label__leaf { background: radial-gradient(ellipse at center, var(--leaf-night), transparent 70%); }

  .brand {
    position: absolute; left: 0; right: 0;
    top: var(--logo-top, 13%);
    font-family: "Cinzel", serif;
    font-weight: 400;
    line-height: 0.9;
  }
  .label--day .brand { color: var(--sage); }
  .label--night .brand { color: var(--gold); }
  .brand__initials { display: block; font-size: 1.5em; }
  .brand__word { display: block; font-size: 0.6em; letter-spacing: 0.04em; }

  .product {
    position: absolute; left: 1%; right: 1%;
    top: var(--title-top, 41%);
    font-family: "Cinzel", serif;
    font-weight: 700;
    font-size: var(--title);
    line-height: var(--lh);
  }
  .product__name {
    display: block;
    white-space: nowrap;
    background: linear-gradient(180deg, var(--gold-light), var(--gold) 55%, var(--gold-deep));
    -webkit-background-clip: text;
    background-clip: text;
    color: transparent;
  }
  .product__scent {
    display: block;
    margin-top: 4px;
    font-family: "Montserrat", sans-serif;
    font-weight: 500;
    font-size: var(--scent, 12px);
    line-height: 1.4;
    color: var(--gold);
  }
  .size {
    position: absolute; left: 0; right: 0; bottom: 3%;
    font-family: "Cinzel", serif;
    font-weight: 700;
    font-size: var(--size, 9px);
    line-height: 1;
    color: var(--gold);
  }
</style>
</head>
<body>
<main class="label-set">

  <article class="label label--day" style="left:40px;top:52px;width:196px;height:245px;--fs:24px;--title:18px;--lh:31px;--title-top:41%;">
    <div class="label__leaf" role="img" aria-label="Faint leafy branch illustration"></div>
    <div class="brand"><span class="brand__initials">TK</span><span class="brand__word">VESSA</span></div>
    <h2 class="product"><span class="product__name">Glycolic<br>Cleanser</span></h2>
    <p class="size">4oz</p>
  </article>

  <article class="label label--day" style="left:262px;top:51px;width:197px;height:246px;--fs:24px;--title:18px;--lh:31px;--title-top:41%;">
    <div class="label__leaf" role="img" aria-label="Faint leafy branch illustration"></div>
    <div class="brand"><span class="brand__initials">TK</span><span class="brand__word">VESSA</span></div>
    <h2 class="product"><span class="product__name">Cleansing<br>Oil</span></h2>
    <p class="size">4oz</p>
  </article>

  <article class="label label--day" style="left:521px;top:66px;width:169px;height:218px;--fs:20px;--logo-top:14%;--title:16px;--lh:29px;--title-top:40%;">
    <div class="label__leaf" role="img" aria-label="Faint leafy branch illustration"></div>
    <div class="brand"><span class="brand__initials">TK</span><span class="brand__word">VESSA</span></div>
    <h2 class="product"><span class="product__name">Vitamin C<br>Day Serum</span></h2>
    <p class="size">2oz</p>
  </article>

  <article class="label label--day" style="left:722px;top:64px;width:171px;height:221px;--fs:20px;--logo-top:14%;--title:15px;--lh:29px;--title-top:40%;">
    <div class="label__leaf" role="img" aria-label="Faint leafy branch illustration"></div>
    <div class="brand"><span class="brand__initials">TK</span><span class="brand__word">VESSA</span></div>
    <h2 class="product"><span class="product__name">Stem Cell C<br>Day Serum</span></h2>
    <p class="size">2oz</p>
  </article>

  <article class="label label--day" style="left:32px;top:340px;width:222px;height:147px;--fs:16px;--logo-top:10%;--title:12px;--lh:22px;--title-top:39%;--size:7px;">
    <div class="label__leaf" role="img" aria-label="Faint leafy branch illustration"></div>
    <div class="brand"><span class="brand__initials">TK</span><span class="brand__word">VESSA</span></div>
    <h2 class="product"><span class="product__name">Stem Cell C<br>Day Serum</span></h2>
    <p class="size">2oz</p>
  </article>

  <article class="label label--day" style="left:299px;top:365px;width:146px;height:98px;--fs:12px;--logo-top:6%;--title:10px;--lh:19px;--title-top:36%;--size:5px;">
    <div class="label__leaf" role="img" aria-label="Faint leafy branch illustration"></div>
    <div class="brand"><span class="brand__initials">TK</span><span class="brand__word">VESSA</span></div>
    <h2 class="product"><span class="product__name">Vitamin C Day<br>Eye Cream</span></h2>
    <p class="size">0.5oz</p>
  </article>

  <article class="label label--day" style="left:493px;top:365px;width:146px;height:98px;--fs:12px;--logo-top:6%;--title:10px;--lh:19px;--title-top:36%;--size:5px;">
    <div class="label__leaf" role="img" aria-label="Faint leafy branch illustration"></div>
    <div class="brand"><span class="brand__initials">TK</span><span class="brand__word">VESSA</span></div>
    <h2 class="product"><span class="product__name">Honey<br>Lip Balm</span></h2>
    <p class="size">0.5oz</p>
  </article>

  <article class="label label--night" style="left:30px;top:549px;width:177px;height:221px;--fs:20px;--logo-top:14%;--title:16px;--lh:27px;--title-top:41%;">
    <div class="label__leaf" role="img" aria-label="Faint leafy branch illustration"></div>
    <div class="brand"><span class="brand__initials">TK</span><span class="brand__word">VESSA</span></div>
    <h2 class="product"><span class="product__name">Retinol<br>Night Serum</span><span class="product__scent">Neroli</span></h2>
    <p class="size">2oz</p>
  </article>

  <article class="label label--night" style="left:242px;top:549px;width:178px;height:222px;--fs:20px;--logo-top:14%;--title:16px;--lh:27px;--title-top:41%;">
    <div class="label__leaf" role="img" aria-label="Faint leafy branch illustration"></div>
    <div class="brand"><span class="brand__initials">TK</span><span class="brand__word">VESSA</span></div>
    <h2 class="product"><span class="product__name">Retinol<br>Night Serum</span><span class="product__scent">Neroli</span></h2>
    <p class="size">2oz</p>
  </article>

  <article class="label label--night" style="left:455px;top:533px;width:199px;height:248px;--fs:23px;--logo-top:14%;--title:17px;--lh:30px;--title-top:41%;">
    <div class="label__leaf" role="img" aria-label="Faint leafy branch illustration"></div>
    <div class="brand"><span class="brand__initials">TK</span><span class="brand__word">VESSA</span></div>
    <h2 class="product"><span class="product__name">Coconut<br>Charcoal<br>Scrub</span></h2>
    <p class="size">4oz</p>
  </article>

  <article class="label label--night" style="left:688px;top:535px;width:199px;height:248px;--fs:23px;--logo-top:14%;--title:18px;--lh:30px;--title-top:41%;">
    <div class="label__leaf" role="img" aria-label="Faint leafy branch illustration"></div>
    <div class="brand"><span class="brand__initials">TK</span><span class="brand__word">VESSA</span></div>
    <h2 class="product"><span class="product__name">Enzyme<br>Night Cream</span></h2>
    <p class="size">4oz</p>
  </article>

  <article class="label label--night" style="left:36px;top:853px;width:118px;height:171px;--fs:12px;--logo-top:12%;--title:9.5px;--lh:17px;--title-top:36%;--size:5px;">
    <div class="label__leaf" role="img" aria-label="Faint leafy branch illustration"></div>
    <div class="brand"><span class="brand__initials">TK</span><span class="brand__word">VESSA</span></div>
    <h2 class="product"><span class="product__name">Eye Renewal<br>Night Serum</span></h2>
    <p class="size">0.5oz</p>
  </article>

  <article class="label label--day" style="left:171px;top:822px;width:222px;height:294px;--fs:26px;--logo-top:13%;--title:20px;--lh:35px;--title-top:36%;">
    <div class="label__leaf" role="img" aria-label="Faint leafy branch illustration"></div>
    <div class="brand"><span class="brand__initials">TK</span><span class="brand__word">VESSA</span></div>
    <h2 class="product"><span class="product__name">Enzyme<br>Body Lotion</span><span class="product__scent">Vanilla Almond</span></h2>
    <p class="size">8oz</p>
  </article>

  <article class="label label--day" style="left:423px;top:824px;width:219px;height:291px;--fs:26px;--logo-top:13%;--title:20px;--lh:35px;--title-top:36%;">
    <div class="label__leaf" role="img" aria-label="Faint leafy branch illustration"></div>
    <div class="brand"><span class="brand__initials">TK</span><span class="brand__word">VESSA</span></div>
    <h2 class="product"><span class="product__name">Enzyme<br>Body Lotion</span><span class="product__scent">Mango Lime</span></h2>
    <p class="size">8oz</p>
  </article>

  <article class="label label--day" style="left:673px;top:824px;width:218px;height:291px;--fs:26px;--logo-top:13%;--title:20px;--lh:35px;--title-top:36%;">
    <div class="label__leaf" role="img" aria-label="Faint leafy branch illustration"></div>
    <div class="brand"><span class="brand__initials">TK</span><span class="brand__word">VESSA</span></div>
    <h2 class="product"><span class="product__name">Enzyme<br>Body Lotion</span><span class="product__scent">Lavender</span></h2>
    <p class="size">8oz</p>
  </article>

</main>
</body>
</html>
```